IT services company needs a business card designed

-2 sided business card.-Front is going to be the logo raised (3D floating effect) on a black background. Make the logos spider web shiny silver and keep the spider the same design. -Back needs to have the following information:Darrel Sotho, Managing Partner, Cell: 738-402-1954, Website: Plankhorn.com, Email: Darrel@Plankhorn.com
Target Market(s)
IT Services
Industry/Entity Type
It Company
Contact Information for Business Card
-2 sided business card.
-Front is going to be the logo raised (3D floating effect) on a black background. Make the logos spider web shiny silver and keep the spider the same design.
-Back needs to have the following information:
Darrel Sotho, Managing Partner, Cell: 738-402-1954, Website: Plankhorn.com, Email: Darrel@Plankhorn.com

```html
<!DOCTYPE html>
<html lang="en">
<head>
<meta charset="utf-8">
<title>Plankhorn Business Card</title>
<link href="https://fonts.googleapis.com/css2?family=Montserrat:wght@400;500;700&display=swap" rel="stylesheet">
<style>
  :root{
    --stage:#2b2d31;
    --card-white:#ffffff;
    --card-black:#0b0b0c;
    --ink:#141414;
    --ink-soft:#3a3a3a;
    --accent:#2ea3e3;
    --silver:#e6e8ea;
  }
  *{margin:0;padding:0;box-sizing:border-box;}
  html,body{width:1200px;height:960px;overflow:hidden;background:var(--stage);}
  body{font-family:"Montserrat",sans-serif;position:relative;}

  .card{position:absolute;left:300px;width:600px;height:343px;border-radius:22px;overflow:hidden;}
  .card-back{top:90px;background:var(--card-white);}
  .card-front{top:527px;background:var(--card-black);}

  .back-shape{position:absolute;inset:0;}

  .brand{position:absolute;display:flex;align-items:center;gap:10px;}
  .brand-name{font-weight:700;letter-spacing:3px;}
  .brand-dot{border-radius:50%;}

  .card-back .brand{left:34px;top:86px;}
  .card-back .brand-name{font-size:30px;color:var(--ink);}
  .card-back .brand-dot{width:12px;height:12px;background:var(--accent);}

  .divider{position:absolute;left:0;top:0;}

  .contact{position:absolute;left:318px;top:78px;}
  .person-name{font-size:25px;font-weight:700;color:var(--ink);letter-spacing:1px;}
  .person-name .surname{color:var(--accent);font-weight:500;}
  .person-title{font-size:14px;font-weight:500;color:var(--ink-soft);letter-spacing:2px;margin:2px 0 16px;}
  .contact-list{list-style:none;}
  .contact-item{display:flex;align-items:center;gap:10px;font-size:15px;color:var(--ink);margin-bottom:6px;}
  .contact-icon{width:16px;height:16px;flex:none;}

  .front-pattern{position:absolute;inset:0;}
  .card-front .brand{left:50%;top:50%;transform:translate(-50%,-50%);}
  .card-front .brand-name{font-size:46px;color:var(--silver);}
  .card-front .brand-dot{width:16px;height:16px;background:var(--silver);}
</style>
</head>
<body>

<section class="card card-back">
  <svg class="back-shape" width="600" height="343" viewBox="0 0 600 343">
    <path d="M0 150 C 40 260, 200 320, 420 343 L0 343 Z" fill="var(--card-black)"/>
    <path d="M0 132 C 46 250, 210 312, 436 343" fill="none" stroke="var(--accent)" stroke-width="7"/>
  </svg>

  <div class="brand">
    <span class="brand-name">PLANKHORN</span>
    <span class="brand-dot"></span>
  </div>

  <svg class="divider" width="600" height="343" viewBox="0 0 600 343">
    <line x1="300" y1="70" x2="268" y2="238" stroke="var(--ink)" stroke-width="1.5"/>
  </svg>

  <div class="contact">
    <p class="person-name">DARREL <span class="surname">SOTHO</span></p>
    <p class="person-title">MANAGING PARTNER</p>
    <ul class="contact-list">
      <li class="contact-item">
        <svg class="contact-icon" viewBox="0 0 16 16"><rect x="4" y="1" width="8" height="14" rx="1.5" fill="none" stroke="var(--accent)" stroke-width="1.8"/><circle cx="8" cy="12.3" r="0.9" fill="var(--accent)"/></svg>
        738-402-1954
      </li>
      <li class="contact-item">
        <svg class="contact-icon" viewBox="0 0 16 16"><rect x="1" y="3" width="14" height="10" rx="1" fill="var(--accent)"/><path d="M1.5 3.5 L8 9 L14.5 3.5" fill="none" stroke="#fff" stroke-width="1.3"/></svg>
        Darrel@Plankhorn.com
      </li>
      <li class="contact-item">
        <svg class="contact-icon" viewBox="0 0 16 16"><circle cx="8" cy="8" r="7.5" fill="var(--accent)"/><ellipse cx="8" cy="8" rx="3" ry="7" fill="none" stroke="#fff" stroke-width="1.1"/><line x1="1" y1="8" x2="15" y2="8" stroke="#fff" stroke-width="1.1"/></svg>
        www.plankhorn.com
      </li>
    </ul>
  </div>
</section>

<section class="card card-front">
  <svg class="front-pattern" width="600" height="343" viewBox="0 0 600 343" role="img" aria-label="Faint dark geometric facet pattern across the black card face">
    <defs>
      <radialGradient id="facetGlow" cx="50%" cy="45%" r="65%">
        <stop offset="0" stop-color="#1c1d20"/>
        <stop offset="1" stop-color="#070708"/>
      </radialGradient>
    </defs>
    <rect width="600" height="343" fill="url(#facetGlow)"/>
  </svg>

  <div class="brand">
    <span class="brand-name">PLANKHORN</span>
    <span class="brand-dot"></span>
  </div>
</section>

</body>
</html>
```